Business card design for new, innovative company - BluePlinth

We are a new company looking for a business card design that is fun, different and quirky. Must use corporate colour green - CMYK C:55, M:0, Y:100, K:0, and corporate colour grey - C:0, M:0, Y: 0, K:70.

We have developed the first real time data application, in which people are able to profile the data of their existing customers in order to pull out more good fit clients to direct their marketing activities at.

Industry/Entity Type

Marketing

Requirements
Must have
• Logo, name, title, telephone number, fax number, email, website, address

```html
<!DOCTYPE html>
<html lang="en">
<head>
<meta charset="utf-8">
<title>BluePlinth – Business Card</title>
<link rel="stylesheet" href="https://fonts.googleapis.com/css2?family=Arimo:wght@400;700&display=swap">
<style>
  :root {
    --brand-green: #62b947;
    --brand-grey: #6d6e71;
    --card-white: #f4f4f4;
    --backdrop: #2a2a2a;
    --text-soft: #ffffff;
  }
  * { margin: 0; padding: 0; box-sizing: border-box; }
  html, body {
    width: 1200px;
    height: 900px;
    overflow: hidden;
    background: var(--backdrop);
    font-family: "Arimo", Arial, sans-serif;
  }
  .canvas {
    position: relative;
    width: 1200px;
    height: 900px;
    display: flex;
    align-items: center;
    justify-content: center;
    gap: 40px;
  }
  .card {
    position: relative;
    width: 520px;
    height: 300px;
    border-radius: 4px;
    overflow: hidden;
  }

  /* Back of card */
  .card-back {
    background: var(--brand-green);
    display: flex;
    flex-direction: column;
    align-items: center;
    justify-content: center;
    gap: 22px;
  }
  .card-back .brand-square {
    width: 110px;
    height: 110px;
    border-radius: 22px;
    background: var(--text-soft);
  }
  .card-back .brand-name {
    color: var(--text-soft);
    font-weight: 700;
    font-size: 34px;
    letter-spacing: -0.5px;
  }
  .card-back .website {
    color: var(--text-soft);
    font-size: 15px;
    letter-spacing: 0.3px;
  }

  /* Front of card */
  .card-front {
    background: var(--card-white);
  }
  .card-front .wordmark {
    position: absolute;
    left: 28px;
    top: 40px;
    color: var(--brand-green);
    font-weight: 700;
    font-size: 50px;
    letter-spacing: -2px;
    line-height: 1;
  }
  .card-front .side-panel {
    position: absolute;
    right: 22px;
    top: 22px;
    width: 150px;
    height: 256px;
    border-radius: 14px;
    background: var(--brand-green);
  }
  .contact {
    position: absolute;
    left: 30px;
    top: 128px;
    color: var(--brand-grey);
    font-size: 13.5px;
    line-height: 1.35;
    letter-spacing: 0.3px;
  }
  .contact .person-name {
    color: var(--brand-green);
    font-weight: 700;
    font-size: 16px;
    margin-bottom: 6px;
  }
  .contact .address {
    margin-top: 22px;
  }
</style>
</head>
<body>
  <main class="canvas">
    <section class="card card-back" aria-label="Business card, back">
      <div class="brand-square" aria-hidden="true"></div>
      <div class="brand-name">BluePlinth</div>
      <div class="website">www.blueplinth.com</div>
    </section>

    <section class="card card-front" aria-label="Business card, front">
      <div class="wordmark">BluePlinth</div>
      <div class="side-panel" aria-hidden="true"></div>
      <div class="contact">
        <p class="person-name">Jenna Calloway</p>
        <p>M: 07700900482</p>
        <p>T: 01632 960735</p>
        <p>E: jenna.calloway@northfenworks.com</p>
        <div class="address">
          <p>22c Larkfield Avenue</p>
          <p>Wexley, Norfolk&nbsp; NR9 4QT</p>
        </div>
      </div>
    </section>
  </main>
</body>
</html>
```